Popup Nightclub Grand Opening Flyer

We need to design a flyer for the grand opening of an upscale, exclusive nightclub called "Lanternfall". The design needs to be chic and exclusive. The background should be black and the text should primarily be white. We like minimalist designs.

Here is the text for the flyer
-
Velvetrope Atlanta Presents

Lanternfall (LOGO)

A Popup Nightclub Experience
For one night Only

Friday, October 18, 2013
Party begins at 9PM

INVITE ONLY

See invitation for location details
(Velvetrope Atlanta logo)

-
Examples we like

http://cdn2-b.brivelpost.com/sites/default/files/styles/image_content_width/hash/3d/fa/1472093815_4471_flyer.jpg?itok=R8kqWm2z

http://api.plovra.com/files/7Kqq-Tr82XXB3pQzJvmtR5HL2W719E4nbRtC6KLd4HsfM8Y2qTDK-VmjwDoNqLX4QBzTHD9nakRbVx3m-Pfq8htc3MDTWr5p4/2zelSaturdays.jpg

http://quenmar.com/wp-content/uploads/yootheme/widgetkit/gallery/2zel/2zel-gen_vroom4-01.jpg

Hi All, one thing that we are seeing that we don't like is on over emphasis on the phrase "a popup nightclub experience" please don't make this the largest thing on the flyer

Target Market(s)

Target market is 25-35 year olds who are affluent (rich) and like luxury brands

Requirements
Must have
• Dark Background
Nice to have
• Velvetrope Logo on the bottom
Modern text that isn't curvy
Should not have
• Curved text

```html
<!DOCTYPE html>
<html lang="en">
<head>
<meta charset="utf-8">
<title>Lanternfall Nightclub — Velvetrope Atlanta</title>
<link rel="stylesheet" href="https://fonts.googleapis.com/css2?family=Jost:wght@300;400&display=swap">
<style>
  :root {
    --ink: #f2f2f2;
    --ink-soft: #cfcfcf;
    --ink-faint: #7a7a7a;
    --divider: #8a8a8a;
    --bg-deep: #050505;
    --bg-mid: #1c1c1c;
    --bg-lift: #2c2c2c;
    --mark: #bdbdbd;
  }
  * { margin: 0; padding: 0; box-sizing: border-box; }
  html, body {
    width: 901px;
    height: 1200px;
    overflow: hidden;
    background: var(--bg-deep);
  }
  .flyer {
    position: relative;
    width: 901px;
    height: 1200px;
    overflow: hidden;
    font-family: "Jost", "Helvetica Neue", Arial, sans-serif;
    font-weight: 300;
    color: var(--ink);
    text-align: center;
  }
  .flyer__backdrop {
    position: absolute;
    inset: 0;
    background:
      radial-gradient(ellipse 70% 55% at 50% 38%, var(--bg-lift) 0%, var(--bg-mid) 45%, var(--bg-deep) 100%);
  }
  .presenter {
    position: absolute;
    top: 112px;
    left: 0;
    width: 100%;
    display: flex;
    justify-content: center;
    align-items: center;
    gap: 12px;
  }
  .presenter__dot {
    width: 12px;
    height: 12px;
    border-radius: 50%;
    background: var(--ink-soft);
  }
  .presenter__name {
    font-size: 24px;
    letter-spacing: 0.04em;
    text-transform: uppercase;
    color: var(--ink-soft);
  }
  .presents {
    position: absolute;
    top: 191px;
    left: 0;
    width: 100%;
    font-size: 13px;
    letter-spacing: 0.1em;
    color: var(--ink-soft);
  }
  .venue {
    position: absolute;
    top: 725px;
    left: 0;
    width: 100%;
  }
  .venue__disc {
    display: block;
    width: 128px;
    height: 128px;
    margin: 0 auto 38px;
    border-radius: 50%;
    background: var(--mark);
  }
  .venue__name {
    font-size: 44px;
    line-height: 1;
    letter-spacing: 0.22em;
    text-transform: uppercase;
    padding-left: 0.22em;
  }
  .venue__type {
    margin-top: 12px;
    font-size: 20px;
    line-height: 1;
    letter-spacing: 0.2em;
    text-transform: uppercase;
    padding-left: 0.2em;
  }
  .details {
    position: absolute;
    top: 1047px;
    left: 0;
    width: 100%;
    list-style: none;
  }
  .details__row {
    display: flex;
    justify-content: center;
    align-items: center;
    font-size: 19px;
    line-height: 1;
    text-transform: uppercase;
    color: var(--ink-soft);
  }
  .details__row + .details__row { margin-top: 21px; }
  .details__sep {
    display: inline-block;
    width: 1px;
    height: 16px;
    margin: 0 24px;
    background: var(--divider);
  }
  .note {
    position: absolute;
    top: 1141px;
    left: 0;
    width: 100%;
    font-size: 10px;
    letter-spacing: 0.04em;
    color: var(--ink-faint);
  }
</style>
</head>
<body>
  <main class="flyer">
    <div class="flyer__backdrop" role="img" aria-label="Dark charcoal backdrop of softly blurred glittering light"></div>

    <header class="presenter">
      <span class="presenter__dot"></span>
      <span class="presenter__name">Velvetrope Atlanta</span>
    </header>
    <p class="presents">Presents</p>

    <section class="venue">
      <span class="venue__disc"></span>
      <h1 class="venue__name">Lanternfall</h1>
      <p class="venue__type">Nightclub</p>
    </section>

    <ul class="details">
      <li class="details__row">
        <span>A Popup Nightclub Experience</span>
        <span class="details__sep"></span>
        <span>For One Night Only</span>
      </li>
      <li class="details__row">
        <span>Friday, October 18, 2013</span>
        <span class="details__sep"></span>
        <span>Party Begins at 9PM</span>
        <span class="details__sep"></span>
        <span>Invite Only</span>
      </li>
    </ul>

    <p class="note">See invitation for location details</p>
  </main>
</body>
</html>
```